Landing Page Design for Adult Dating Age Verification (18+)

The objective of this task is to design a visually appealing pre-landing page for the adult dating site "Plumvelle (site: https://plumvelle.example/)" with an age verification mechanism. The pre-landing page will feature two buttons that redirect visitors to the main offer. The design should also include a footer block that includes links to the terms of use, privacy policy, and contact us pages.

Design Requirements:
Develop an age verification section prominently displayed on the pre-landing page.
Design the section to include two buttons labeled "Yes" and "No" for visitors to confirm their age.
Ensure the section is visually appealing and clearly communicates the purpose of age verification.

Visual Appeal:
Create a visually appealing design that aligns with the branding and theme of the "Plumvelle" adult dating site.
Use suitable color schemes, typography, and graphics to enhance the overall visual appeal of the pre-landing page.

Layout and Navigation:
Design an engaging and intuitive layout that encourages visitors to interact with the page and proceed to the main offer.
Ensure clear and visible navigation elements that direct visitors to the main offer or provide additional information.

Responsive Design:
Develop a responsive design that provides a seamless user experience across various devices, including desktop and mobile.
Ensure the design elements and layout adapt well to different screen sizes and resolutions.

File Formats and Assets:
Deliver the final design in PSD, AI, or Sketch format, ensuring that the files are well-organized and layered.
Include any necessary images or assets used in the design, ensuring they are of high quality and optimized for web use.

```html
<!DOCTYPE html>
<html lang="en">
<head>
<meta charset="utf-8">
<title>Plumvelle — Age Verification</title>
<link rel="stylesheet" href="https://fonts.googleapis.com/css2?family=Gloock&family=Josefin+Sans:wght@300&display=swap">
<style>
  :root {
    --lavender: #d5b3d6;
    --lavender-btn: #d2b0d4;
    --white: #ffffff;
    --shade-dark: #2e2c31;
    --shade-mid: #6f6a6c;
    --skin: #b58a78;
    --skin-light: #d2ab98;
  }
  * { margin: 0; padding: 0; box-sizing: border-box; }
  html, body { width: 1200px; height: 687px; overflow: hidden; }
  body { position: relative; font-family: "Gloock", serif; color: var(--white); background: var(--shade-dark); }

  .hero {
    position: absolute; left: 0; top: 0; width: 1200px; height: 624px;
    background:
      radial-gradient(ellipse 260px 320px at 960px 330px, var(--skin-light) 0%, rgba(181,138,120,0.6) 45%, rgba(46,44,49,0) 100%),
      radial-gradient(ellipse 420px 120px at 330px 300px, rgba(181,138,120,0.55) 0%, rgba(46,44,49,0) 100%),
      linear-gradient(180deg, var(--shade-mid) 0%, #4b474a 55%, var(--shade-dark) 100%);
  }
  .hero-scrim { position: absolute; inset: 0; background: rgba(20, 18, 22, 0.25); }

  .brand { position: absolute; left: 100px; top: 26px; display: flex; align-items: center; gap: 14px; }
  .brand-dot { width: 56px; height: 56px; border-radius: 50%; background: var(--lavender); }
  .brand-name { font-size: 34px; line-height: 1; color: var(--white); font-weight: 400; }

  .gate { position: absolute; left: 0; top: 107px; width: 1200px; text-align: center; }
  .gate-icon { display: block; margin: 0 auto; width: 102px; height: 110px; }
  .gate-title { margin-top: 27px; font-size: 44px; line-height: 44px; font-weight: 400; letter-spacing: 0.2px; }
  .gate-note { margin-top: 22px; font-family: "Josefin Sans", sans-serif; font-weight: 300; font-size: 17.5px; letter-spacing: 0.5px; }

  .gate-actions { position: absolute; left: 431px; top: 412px; display: flex; gap: 19px; }
  .btn {
    display: flex; align-items: center; justify-content: center;
    width: 160px; height: 44px; border-radius: 22px;
    font-family: "Gloock", serif; font-size: 12.5px; color: var(--white);
    text-decoration: none; letter-spacing: 0.3px;
  }
  .btn-yes { background: var(--lavender-btn); }
  .btn-no { border: 1px solid var(--white); }

  .footer {
    position: absolute; left: 0; top: 624px; width: 1200px; height: 63px;
    background: var(--lavender); display: flex; align-items: center;
  }
  .footer a { position: absolute; color: var(--white); text-decoration: none; font-size: 12px; letter-spacing: 0.4px; }
  .footer .link-privacy { left: 103px; }
  .footer .link-terms { left: 0; width: 1200px; text-align: center; }
  .footer .link-contact { right: 100px; }
</style>
</head>
<body>
  <div class="hero" role="img" aria-label="Photograph of a woman in a white shirt lying on a bed with pillows and a fluffy rug">
    <div class="hero-scrim"></div>
  </div>

  <header class="brand">
    <span class="brand-dot"></span>
    <span class="brand-name">Plumvelle</span>
  </header>

  <main class="gate">
    <svg class="gate-icon" viewBox="0 0 102 110" fill="none" stroke="#ffffff" stroke-width="3" aria-hidden="true">
      <circle cx="28" cy="56" r="27"/>
      <line x1="28" y1="83" x2="28" y2="108"/>
      <line x1="17" y1="97" x2="39" y2="97"/>
      <circle cx="66" cy="36" r="27"/>
      <line x1="85" y1="17" x2="100" y2="2"/>
      <polyline points="88,2 100,2 100,14"/>
    </svg>
    <h1 class="gate-title">The site contains sexually<br>explicit material.</h1>
    <p class="gate-note">ENTER ONLY IF YOU ARE OVER 18</p>
  </main>

  <nav class="gate-actions">
    <a class="btn btn-yes" href="https://plumvelle.example/">I AM OVER 18</a>
    <a class="btn btn-no" href="#">I AM UNDER 18</a>
  </nav>

  <footer class="footer">
    <a class="link-privacy" href="#">PRIVACY POLICY</a>
    <a class="link-terms" href="#">TERMS AND CONDITIONS</a>
    <a class="link-contact" href="#">CONTACT US</a>
  </footer>
</body>
</html>
```